IT Consulting Business Card Design

We need a business card on our company name....which is a IT consulting and staffing company. We also train masters graduates in various IT courses. 70% of the time these cards will be handed out to the graduate students at the universities. 30% for our clients and business partners. We are uploading our company logo...would like to see something that matches our logo or blends with it. Please visit www.brightlanetek.example for more details on logo and colors.

Target Market(s)

70% of the time these cards will be handed out to the graduate students at the universities. 30% for our clients and business partners.

Industry/Entity Type

Business

Contact Information for Business Card

Rafe Tolliverson
Vice-President
Bright Lane Tek Inc
3187 Winslow Drive, Suite 412
Oak Hollow, NJ 07391
rafe@brightlanetek.example
Office : 1-855-217-9038 X 414
Cell number : 908-731-2948

Requirements
Nice to have
• may be company logo and name on the back of the card and detials on the other side...just a thought..!!

```html
<!DOCTYPE html>
<html lang="en">
<head>
<meta charset="utf-8">
<title>Bright Lane Tek – Business Card</title>
<link rel="stylesheet" href="https://fonts.googleapis.com/css2?family=PT+Sans:wght@400;700&family=PT+Sans+Narrow:wght@700&display=swap">
<style>
  :root {
    --brand-red: #e0202a;
    --ink: #333333;
    --muted: #555555;
    --rule: #cccccc;
    --card-white: #ffffff;
    --card-black: #1b1b1b;
    --card-black-edge: #0c0c0c;
    --backdrop: #e9e6e1;
  }
  * { box-sizing: border-box; margin: 0; padding: 0; }
  html, body {
    width: 1200px; height: 1023px; overflow: hidden;
    background: var(--backdrop);
    font-family: "PT Sans", Arial, sans-serif;
  }
  .card {
    position: absolute; left: 280px; width: 640px; height: 366px;
    box-shadow: 0 10px 28px rgba(0,0,0,.25);
  }
  /* Back side */
  .card-back {
    top: 70px;
    background: radial-gradient(ellipse at 50% 35%, #2c2c2c 0%, var(--card-black) 55%, var(--card-black-edge) 100%);
    display: flex; flex-direction: column; align-items: center; justify-content: center;
  }
  .card-back .brand-mark {
    width: 150px; height: 150px; border-radius: 50%;
    background: var(--brand-red); margin-bottom: 26px;
  }
  .card-back .brand-name {
    font-family: "PT Sans Narrow", "Arial Narrow", sans-serif;
    font-weight: 700; font-size: 54px; letter-spacing: 1px;
    color: #ffffff; line-height: 1;
  }
  .card-back .website {
    margin-top: 14px; font-size: 19px; color: #dddddd;
  }
  /* Front side */
  .card-front {
    top: 496px; background: var(--card-white); overflow: hidden;
  }
  .front-brand {
    position: absolute; left: 30px; top: 24px;
    display: flex; align-items: center; gap: 18px;
  }
  .front-brand .brand-mark {
    width: 84px; height: 84px; border-radius: 50%; background: var(--brand-red);
  }
  .front-brand .brand-name {
    font-family: "PT Sans Narrow", "Arial Narrow", sans-serif;
    font-weight: 700; font-size: 38px; color: var(--ink); letter-spacing: .5px;
  }
  .person {
    position: absolute; right: 48px; top: 120px; text-align: right;
  }
  .person .name { font-weight: 700; font-size: 26px; color: var(--brand-red); line-height: 1.1; }
  .person .title { font-size: 15px; color: var(--muted); margin-right: 10px; line-height: 1.3; }
  .divider {
    position: absolute; left: 30px; right: 165px; top: 168px;
    border-top: 1px solid var(--rule);
  }
  .address {
    position: absolute; left: 30px; top: 186px;
    font-size: 15px; font-style: normal; color: var(--ink); line-height: 1.3;
  }
  .contacts {
    position: absolute; left: 30px; top: 234px; list-style: none;
    font-size: 15px; color: var(--ink);
  }
  .contacts li { display: flex; align-items: center; gap: 12px; height: 21px; }
  .contacts svg { width: 16px; height: 16px; flex: none; }
  .tagline-band {
    position: absolute; left: 0; right: 0; bottom: 0; height: 32px;
    background: var(--brand-red); color: #ffffff;
    font-size: 17px; padding: 5px 0 0 34px;
  }
</style>
</head>
<body>
  <section class="card card-back" aria-label="Card back">
    <div class="brand-mark" aria-hidden="true"></div>
    <div class="brand-name">BRIGHT LANE TEK</div>
    <div class="website">www.brightlanetek.example</div>
  </section>

  <section class="card card-front" aria-label="Card front">
    <div class="front-brand">
      <div class="brand-mark" aria-hidden="true"></div>
      <div class="brand-name">BRIGHT LANE TEK</div>
    </div>
    <div class="person">
      <div class="name">Rafe Tolliverson</div>
      <div class="title">Vice-President</div>
    </div>
    <div class="divider"></div>
    <address class="address">
      3187 Winslow Drive, Suite 412<br>
      Oak Hollow, NJ 07391
    </address>
    <ul class="contacts">
      <li>
        <svg viewBox="0 0 16 16" aria-label="Mobile"><circle cx="8" cy="8" r="8" fill="var(--brand-red)"/><rect x="5.5" y="3.5" width="5" height="9" rx="1" fill="none" stroke="#fff" stroke-width="1.2"/></svg>
        908-731-2948
      </li>
      <li>
        <svg viewBox="0 0 16 16" aria-label="Office"><circle cx="8" cy="8" r="8" fill="var(--brand-red)"/><path d="M4 7c0-2 8-2 8 0v1H10V7H6v1H4z M5 9h6v3H5z" fill="#fff"/></svg>
        1-855-217-9038 Ext 414
      </li>
      <li>
        <svg viewBox="0 0 16 16" aria-label="Fax"><circle cx="8" cy="8" r="8" fill="var(--brand-red)"/><rect x="5.5" y="3.5" width="5" height="3" fill="#fff"/><rect x="4" y="7" width="8" height="4" fill="#fff"/><rect x="5.5" y="10" width="5" height="2.5" fill="#fff" stroke="var(--brand-red)" stroke-width=".6"/></svg>
        908-731-2950
      </li>
      <li>
        <svg viewBox="0 0 16 16" aria-label="Email"><circle cx="8" cy="8" r="8" fill="var(--brand-red)"/><rect x="4" y="5" width="8" height="6" fill="#fff"/><path d="M4 5l4 3.5L12 5" fill="none" stroke="var(--brand-red)" stroke-width="1"/></svg>
        rafe@brightlanetek.example
      </li>
    </ul>
    <div class="tagline-band">For all your IT needs...</div>
  </section>
</body>
</html>
```